Business Card

Company: Pine Hollow Nursery.

Use uploaded logo or design one just like it. This is a tree growing operation and really like earth tone colors.

Target Market(s)

Landscaping company's, retail nurseries, and landscape arc.

Industry/Entity Type

Business

Font styles to use
Serif

Requirements
Must have
• Name: Dale Wexford
Title: Owner
Address: 48217 W. 115 Road, Cedarvale, OK 74990
Office: 918-555-3172
Cell: 918-555-6093
Fax: 918-555-4418
email: dalepn@corvalink.net
Pine Hollow Nursery

```html
<!DOCTYPE html>
<html lang="en">
<head>
<meta charset="utf-8">
<title>Pine Hollow Nursery – Business Card</title>
<link rel="stylesheet" href="https://fonts.googleapis.com/css2?family=Lato:wght@300;400;700&display=swap">
<style>
  :root {
    --page-bg: #e9e7e2;
    --card-white: #ffffff;
    --card-shade: #eeeeee;
    --brand-green: #2f8f63;
    --brand-green-dark: #1f6e4a;
    --brand-green-soft: #cfe6da;
    --text-grey: #555a57;
    --rule-grey: #c9cccb;
  }
  * { box-sizing: border-box; margin: 0; padding: 0; }
  html, body {
    width: 1200px; height: 600px; overflow: hidden;
    background: var(--page-bg);
    font-family: "Lato", "Helvetica Neue", Arial, sans-serif;
  }
  .business-card {
    position: absolute; left: 100px; top: 14px;
    width: 1000px; height: 572px;
    border-radius: 26px; overflow: hidden;
    background: radial-gradient(ellipse at 60% 35%, var(--card-white) 0%, var(--card-white) 45%, var(--card-shade) 100%);
    box-shadow: 0 4px 14px rgba(0,0,0,0.12);
  }
  .card-band {
    position: absolute; left: 0; right: 0; bottom: 0; height: 74px;
    background: linear-gradient(180deg, var(--brand-green) 0%, var(--brand-green-dark) 100%);
    border-top: 6px solid var(--rule-grey);
  }
  .brand-block {
    position: absolute; left: 60px; top: 150px; width: 420px;
    display: flex; flex-direction: column; align-items: center;
  }
  .brand-mark {
    width: 150px; height: 150px; border-radius: 50%;
    background: radial-gradient(circle, var(--card-white) 0%, var(--brand-green-soft) 100%);
    margin-bottom: 26px;
  }
  .brand-name {
    font-size: 40px; font-weight: 400; color: var(--brand-green);
    letter-spacing: 0.3px; white-space: nowrap;
  }
  .divider {
    position: absolute; left: 545px; top: 90px; width: 2px; height: 240px;
    background: linear-gradient(180deg, transparent, var(--text-grey) 50%, transparent);
    transform: rotate(14deg); opacity: 0.6;
  }
  .contact-block {
    position: absolute; left: 600px; top: 80px; width: 380px;
    color: var(--text-grey);
  }
  .contact-name {
    font-size: 34px; font-weight: 700; color: var(--brand-green);
  }
  .contact-title {
    font-size: 20px; font-weight: 300; margin-top: 6px; margin-bottom: 22px;
  }
  .contact-address {
    font-size: 21px; font-weight: 300; line-height: 1.35; margin-bottom: 14px;
  }
  .contact-list { list-style: none; }
  .contact-item {
    display: flex; align-items: center; gap: 12px;
    font-size: 21px; font-weight: 300; line-height: 1.45;
  }
  .contact-icon { width: 20px; height: 20px; flex: none; }
  .contact-icon * { fill: var(--brand-green); }
</style>
</head>
<body>
  <main class="business-card">
    <section class="brand-block">
      <div class="brand-mark" role="img" aria-label="Pine Hollow Nursery tree emblem area"></div>
      <p class="brand-name">Pine Hollow Nursery</p>
    </section>

    <div class="divider"></div>

    <section class="contact-block">
      <h1 class="contact-name">Dale Wexford</h1>
      <p class="contact-title">Owner</p>
      <p class="contact-address">48217 W. 115 Road, Cedarvale,<br>OK 74990</p>
      <ul class="contact-list">
        <li class="contact-item">
          <svg class="contact-icon" viewBox="0 0 20 20" aria-hidden="true"><rect x="1" y="1" width="18" height="18" rx="3"/><path d="M6 5h3l1 3-2 1c1 2 2 3 4 4l1-2 3 1v3c-6 0-10-4-10-10z" style="fill:#fff"/></svg>
          <span>918-555-3172 (Office)</span>
        </li>
        <li class="contact-item">
          <svg class="contact-icon" viewBox="0 0 20 20" aria-hidden="true"><rect x="5" y="1" width="10" height="18" rx="2"/><rect x="7" y="3" width="6" height="11" style="fill:#fff"/></svg>
          <span>918-555-6093</span>
        </li>
        <li class="contact-item">
          <svg class="contact-icon" viewBox="0 0 20 20" aria-hidden="true"><rect x="5" y="1" width="10" height="6"/><rect x="1" y="7" width="18" height="9" rx="2"/><rect x="5" y="13" width="10" height="6" style="fill:#fff;stroke:#2f8f63;stroke-width:1.5"/></svg>
          <span>918-555-4418</span>
        </li>
        <li class="contact-item">
          <svg class="contact-icon" viewBox="0 0 20 20" aria-hidden="true"><rect x="1" y="1" width="18" height="18" rx="3"/><path d="M4 6l6 5 6-5v1.5l-6 5-6-5z" style="fill:#fff"/></svg>
          <span>dalepn@corvalink.net</span>
        </li>
      </ul>
    </section>

    <div class="card-band"></div>
  </main>
</body>
</html>
```